Business Card Design for Mabel's Larder

We make food for dogs.
Business Card Design (using the logo designed by you). Our Brand color is a bright canary yellow. For example our signage is predominantly yellow, with the logo in black. I'd like the card also to use that imagery.
Feel free to use the two sides creatively.
Vertical Design is also great.

Industry/Entity Type

Pet food

Contact Information for Business Card

Name, email, website, phone no

Font styles to use
Sans Serif

Colors
59FF00
82FF00
B8FF75
E3FFCB
F4FFEA
FFF300
FFF600
FEFA6F
FFFEC7
FFFEE8

Requirements
Nice to have
• A graphic in the same brush stroke style of the logo shoeing a doggy bowl of food

```html
<!DOCTYPE html>
<html lang="en">
<head>
<meta charset="utf-8">
<title>Mabel's Larder — Business Card</title>
<link rel="stylesheet" href="https://fonts.googleapis.com/css2?family=Oswald:wght@400&family=Roboto:wght@400;500&display=swap">
<style>
  :root {
    --canary: #fde44f;
    --ink: #111111;
    --paper: #ffffff;
    --night: #030303;
    --backdrop: #ffffff;
    --band-light: #b3b3b3;
    --band-dark: #1a1a1a;
  }
  * { margin: 0; padding: 0; box-sizing: border-box; }
  html, body {
    width: 1200px; height: 2361px; overflow: hidden;
    background: var(--backdrop);
  }
  .stage { position: relative; width: 1200px; height: 2361px; }
  .card {
    position: absolute; left: 187px; width: 826px; height: 472px;
    overflow: hidden;
    box-shadow: 0 6px 14px rgba(0,0,0,0.28);
  }
  .card--front { top: 672px; background: var(--paper); }
  .card--back { top: 1210px; background: var(--night); }
  .card__shapes { position: absolute; inset: 0; width: 100%; height: 100%; }
  .brand-name {
    position: absolute; left: 0; right: 0; text-align: center;
    font-family: 'Oswald', sans-serif; font-weight: 400;
    letter-spacing: 0.5px; white-space: nowrap;
  }
  .card--front .brand-name { top: 118px; font-size: 50px; color: var(--ink); }
  .card--back .brand-name { top: 226px; font-size: 40px; color: var(--canary); }
  .card__tagname {
    position: absolute; left: 186px; top: 313px;
    font-family: 'Roboto', sans-serif; font-weight: 500;
    font-size: 26px; color: var(--ink); letter-spacing: 0.5px;
  }
  .card__divider {
    position: absolute; left: 423px; top: 282px; width: 2px; height: 146px;
    background: var(--ink);
  }
  .contact { position: absolute; left: 453px; top: 318px; list-style: none; }
  .contact__item {
    display: flex; align-items: center; height: 27px;
    font-family: 'Roboto', sans-serif; font-size: 17px; color: var(--ink);
  }
  .contact__icon { width: 18px; height: 18px; margin-right: 17px; flex: none; }
</style>
</head>
<body>
<main class="stage">

  <section class="card card--front" aria-label="Card front">
    <svg class="card__shapes" viewBox="0 0 826 472" aria-hidden="true">
      <defs>
        <linearGradient id="band-fade" x1="0" y1="0" x2="1" y2="0">
          <stop offset="0" stop-color="var(--band-light)"/>
          <stop offset="0.5" stop-color="#5a5a5a"/>
          <stop offset="1" stop-color="var(--band-dark)"/>
        </linearGradient>
      </defs>
      <path d="M0 322 Q400 110 826 328 L826 334 Q400 140 0 360 Z" fill="url(#band-fade)"/>
      <path d="M0 362 Q400 140 826 336 L826 472 L0 472 Z" fill="var(--canary)"/>
    </svg>
    <div class="brand-name">MABEL'S LARDER</div>
    <div class="card__tagname">MABEL'S LARDER</div>
    <div class="card__divider"></div>
    <ul class="contact">
      <li class="contact__item">
        <svg class="contact__icon" viewBox="0 0 24 24" aria-hidden="true"><path fill="#111" d="M6.6 10.8a15.1 15.1 0 0 0 6.6 6.6l2.2-2.2c.3-.3.7-.4 1-.2 1.1.4 2.3.6 3.6.6.6 0 1 .4 1 1V20c0 .6-.4 1-1 1A17 17 0 0 1 3 4c0-.6.4-1 1-1h3.5c.6 0 1 .4 1 1 0 1.3.2 2.5.6 3.6.1.3 0 .7-.2 1z"/></svg>
        1234567890
      </li>
      <li class="contact__item">
        <svg class="contact__icon" viewBox="0 0 24 24" aria-hidden="true"><rect x="2" y="5" width="20" height="14" fill="#111"/><path d="M2 5l10 8 10-8M2 19l7-7M22 19l-7-7" stroke="var(--canary)" stroke-width="1.6" fill="none"/></svg>
        infoyourmailthere@mailhost.com
      </li>
      <li class="contact__item">
        <svg class="contact__icon" viewBox="0 0 24 24" aria-hidden="true"><circle cx="12" cy="12" r="9.5" fill="#111"/><g stroke="var(--canary)" stroke-width="1.3" fill="none"><ellipse cx="12" cy="12" rx="4" ry="9.5"/><path d="M2.5 12h19M4 7h16M4 17h16"/></g></svg>
        www.yourwebsitethere.com
      </li>
    </ul>
  </section>

  <section class="card card--back" aria-label="Card back">
    <div class="brand-name">MABEL'S LARDER</div>
  </section>

</main>
</body>
</html>
```